Beacon Guard Services

Our Company is a security business which needs a cut edge design, the final product should have all relevant information and maintain a bold but modern and professional look.

Target Market(s)

A cut edge design which will attract any audience

Industry/Entity Type

Security

Contact Information for Business Card

BEACON GUARD SERVICES

Daniel Hofstra
Operations Manager
Phone: 0412 739 215

Email: info@beaconguard.com.au
Web: www.beaconguard.com.au

Requirements
Must have
• Must be double sided and contain all relevant information and the company logo.

```html
<!DOCTYPE html>
<html lang="en">
<head>
<meta charset="utf-8">
<title>Beacon Guard Services – Business Card</title>
<link rel="stylesheet" href="https://fonts.googleapis.com/css2?family=Open+Sans:wght@400;600;700;800&display=swap">
<style>
  :root {
    --backdrop: #e7e9ea;
    --card-white: #fdfdfd;
    --card-slate: #4f6b72;
    --card-edge: #ffffff;
    --brand-dark: #3d5b63;
    --brand-orange: #f08a1c;
    --ink-dark: #262d30;
    --ink-light: #ffffff;
    --shadow: rgba(30, 40, 45, 0.25);
  }
  * { box-sizing: border-box; margin: 0; padding: 0; }
  html, body {
    width: 1200px; height: 951px; overflow: hidden;
    background: var(--backdrop);
    font-family: "Open Sans", Arial, sans-serif;
  }
  .canvas { position: relative; width: 1200px; height: 951px; }

  .card {
    position: absolute;
    width: 640px; height: 372px;
    border-radius: 26px;
    box-shadow: 0 12px 30px var(--shadow);
  }

  /* Front side */
  .card-front {
    left: 80px; top: 80px;
    background: radial-gradient(ellipse at 60% 35%, #ffffff 0%, #f1f2f3 70%, #e9ebec 100%);
  }
  .front-mark {
    position: absolute; left: 0; right: 0; top: 120px;
    display: flex; align-items: center; justify-content: center; gap: 14px;
  }
  .mark-dot {
    width: 26px; height: 26px; border-radius: 50%;
    background: var(--brand-orange);
  }
  .brand-name {
    font-weight: 800; color: var(--brand-dark);
    letter-spacing: 1px;
  }
  .front-mark .brand-name { font-size: 52px; }
  .front-url {
    position: absolute; left: 0; right: 0; top: 300px;
    text-align: center; font-size: 22px; font-weight: 600;
    letter-spacing: 1.5px; color: var(--ink-dark);
  }

  /* Back side */
  .card-back {
    left: 470px; top: 470px;
    background: var(--card-edge);
    padding: 12px;
  }
  .back-panel {
    position: relative; width: 100%; height: 100%;
    background: var(--card-slate); border-radius: 16px;
    color: var(--ink-light);
  }
  .back-mark {
    position: absolute; left: 34px; top: 72px;
    display: flex; align-items: center; gap: 10px;
  }
  .back-mark .mark-dot { width: 18px; height: 18px; }
  .back-mark .brand-name { font-size: 32px; color: #ffffff; }

  .holder { position: absolute; left: 360px; top: 76px; }
  .holder-name { font-size: 22px; font-weight: 600; }
  .holder-role { font-size: 15px; font-weight: 600; margin-top: -2px; }

  .address {
    position: absolute; left: 40px; top: 212px;
    display: flex; gap: 8px; font-size: 17px; font-weight: 700; line-height: 22px;
  }
  .contacts {
    position: absolute; left: 262px; top: 210px;
    list-style: none; font-size: 17px; font-weight: 700; line-height: 23px;
  }
  .contacts li { display: flex; align-items: center; gap: 8px; }
  .icon { width: 15px; height: 15px; flex: none; fill: #ffffff; }
  .address .icon { margin-top: 3px; }
</style>
</head>
<body>
<main class="canvas">

  <section class="card card-front" aria-label="Business card front">
    <div class="front-mark">
      <span class="mark-dot"></span>
      <span class="brand-name">BEACON GUARD</span>
    </div>
    <p class="front-url">www.beaconguard.com</p>
  </section>

  <section class="card card-back" aria-label="Business card back">
    <div class="back-panel">
      <div class="back-mark">
        <span class="mark-dot"></span>
        <span class="brand-name">BEACON GUARD</span>
      </div>

      <div class="holder">
        <p class="holder-name">Daniel Hofstra</p>
        <p class="holder-role">director</p>
      </div>

      <div class="address">
        <svg class="icon" viewBox="0 0 16 16" aria-hidden="true"><path d="M8 1 0 8h2v7h4v-5h4v5h4V8h2z"/></svg>
        <p>1480 Harbor Line Rd.<br>Kelston, TX 78115</p>
      </div>

      <ul class="contacts">
        <li>
          <svg class="icon" viewBox="0 0 16 16" aria-hidden="true"><path d="M3 1h3l1 4-2 1a9 9 0 0 0 5 5l1-2 4 1v3c0 1-1 2-2 2A13 13 0 0 1 1 3c0-1 1-2 2-2z"/></svg>
          512-004-3920
        </li>
        <li>
          <svg class="icon" viewBox="0 0 16 16" aria-hidden="true"><path d="M4 1h6l2 2v3H4zM1 7h14v6h-3v2H4v-2H1zM5 11v3h6v-3z"/></svg>
          512-004-3921
        </li>
        <li>
          <svg class="icon" viewBox="0 0 16 16" aria-hidden="true"><path d="M1 3h14v10H1zM2 4v1l6 4 6-4V4z"/></svg>
          info@beaconguard.com
        </li>
        <li>
          <svg class="icon" viewBox="0 0 16 16" aria-hidden="true"><circle cx="8" cy="8" r="7"/></svg>
          www.beaconguard.com
        </li>
      </ul>
    </div>
  </section>

</main>
</body>
</html>
```